Etiketten-Design für Gin
Zielgruppe
Destillieren von GIN (HolgerRUM) / Zielgruppe alle die GIN Lieben :)
Aufgabenstellung
die Grunddatei besteht schon im AI Format, allerdings möchten wir gerne die Highlights in Kupfer haben wie Schrift und Holzfässer, gerne auch eigene Bilder entwerfen. Lediglich das HolgerRUM Logo (Kopf) sollte erhalten bleiben. Bitte die Datei so anlegen das die Highlights in Kupfer gedruckt (Siebdruck) werden können. Transparentes Etikett wäre super! Bei Fragen einfach melden :)

```html
<!DOCTYPE html>
<html lang="de">
<head>
<meta charset="utf-8">
<title>HolgerRUM – Barrel Aged Gin Etikett</title>
<link rel="stylesheet" href="https://fonts.googleapis.com/css2?family=Damion&family=Libre+Baskerville:ital@1&family=Arimo:wght@400&display=swap">
<style>
  :root {
    --label-white: #ffffff;
    --grain-dark: #6e6e6e;
    --grain-mid: #a9a9a9;
    --grain-light: #e6e6e6;
    --brand-grey: #5e5e5e;
    --copper: #cf6a45;
    --copper-deep: #a8482b;
    --copper-light: #e7a98c;
    --spec-copper: #e08a68;
  }
  * { margin: 0; padding: 0; box-sizing: border-box; }
  html, body {
    width: 1200px;
    height: 1196px;
    overflow: hidden;
    background: var(--label-white);
  }
  .label {
    position: relative;
    width: 1200px;
    height: 1196px;
    overflow: hidden;
    background: var(--label-white);
  }
  .wood-grain {
    position: absolute;
    inset: 0;
    background:
      linear-gradient(90deg,
        var(--grain-dark) 0%,
        var(--grain-mid) 6%,
        var(--grain-light) 14%,
        rgba(255,255,255,0) 24%,
        rgba(255,255,255,0) 76%,
        var(--grain-light) 84%,
        var(--grain-mid) 93%,
        var(--grain-dark) 100%),
      linear-gradient(180deg,
        rgba(169,169,169,0.55) 0%,
        rgba(255,255,255,0) 10%,
        rgba(255,255,255,0) 88%,
        rgba(169,169,169,0.55) 100%);
  }
  .portrait {
    position: absolute;
    left: 360px;
    top: 110px;
    width: 580px;
    height: 580px;
  }
  .brand-name {
    position: absolute;
    left: 0;
    top: 600px;
    width: 100%;
    text-align: center;
    font-family: "Damion", cursive;
    font-weight: 400;
    font-size: 290px;
    line-height: 1.1;
    color: var(--brand-grey);
  }
  .product-type {
    position: absolute;
    left: 0;
    top: 976px;
    width: 100%;
    text-align: center;
    font-family: "Libre Baskerville", serif;
    font-style: italic;
    font-weight: 400;
    font-size: 64px;
    line-height: 1;
    color: var(--copper);
  }
  .spec {
    position: absolute;
    top: 1126px;
    font-family: "Arimo", sans-serif;
    font-size: 36px;
    line-height: 1;
    color: var(--spec-copper);
  }
  .spec--abv { left: 96px; }
  .spec--volume { right: 56px; }
</style>
</head>
<body>
  <main class="label">
    <div class="wood-grain" role="img" aria-label="Verwitterte graue Holzmaserung als Hintergrundtextur"></div>
    <svg class="portrait" viewBox="0 0 580 580" role="img" aria-label="Gezeichnetes Kupfer-Porträt des Markengründers">
      <defs>
        <radialGradient id="copper-fill" cx="50%" cy="45%" r="55%">
          <stop offset="0%" stop-color="var(--copper-light)"/>
          <stop offset="60%" stop-color="var(--copper)"/>
          <stop offset="100%" stop-color="var(--copper-deep)" stop-opacity="0"/>
        </radialGradient>
      </defs>
      <ellipse cx="290" cy="285" rx="270" ry="280" fill="url(#copper-fill)"/>
    </svg>
    <h1 class="brand-name">Holger</h1>
    <p class="product-type">Barrel Aged Gin</p>
    <p class="spec spec--abv">45% vol.</p>
    <p class="spec spec--volume">0,5 l</p>
  </main>
</body>
</html>
```